Updated VOLA Brochure for cultural event

We are seeking an updated brochure in a standard 8.5 by 11 size, and we have provided the current brochure and necessary information for inclusion. We desire a fresh new design that conveys a modern and elegant aesthetic. As we anticipate making changes to the brochure periodically, we require an editable program for its creation. Our First Nation Community values our beliefs and appearance, and we hope the brochure will reflect our welcoming nature while standing out from the crowd.
Attached Brochure is from last year
Wants and needs:
Page one. A redesign All the info on the page needs to be there but it needs a face lift.
Page two. Information is attached for that but do need this page editable for future. Join us for an immersive cultural experience at Pelham Creek First Nation (PCFN) community, located in Northeastern BC. We invite you to participate in the Vola Camping Experience, a unique opportunity to forge relationships with our community, connect with our Chief and Council, and engage with industry leaders. Your participation in this grassroots event will earn your company credibility for the work it performs in PCFN territory.

Through this experience, you'll gain an appreciation and understanding of our community and cultural values, while meeting with key office staff, industry C-Suite level executives, industry Indigenous relations staff, and local, regional, and provincial representatives in a positive and welcoming space. The recent Tarrow V. Ontario 2021 decision has significantly shifted how consultation and engagement will be managed on our lands. To help you better understand why managing cumulative effects is essential to PCFN, we welcome you to join us for a three-day camping experience from May 23 to May 26, 2023.

The Vola Camping Experience offers a variety of activities, including a dinner visit to NAH 'B'ilo, the 12,500-year-old cave, where an archeological dig is currently underway, accompanied by our economic development corporation team from Raska Development LP. The event also includes traditional bush camping in elegant teepees/wall tents, dry meat making, and participation in our Pelham Day, a 30+ year cultural education and anti-racism event held on May 25, 2023. During Pelham Day, over 400+ students from School District #47 participate in traditional activities, including moose hide preparation, beaver skinning, archaeology dig, dry-meat making, trapping demonstrations, Bannock on a stick, storytelling, drumming, and tea dance around the campfire to the beat of our drums.

Root yourself to the land, connect with your inner self, and be transformed alongside other important dignitaries as you partake in these multi-sensory experiences on our cultural grounds. This is our second combined camping/Pelham Day experience, and we hope to continue and build on it for future cultural tourism activities such as guided bush camps, hikes, and hunts.

If you are unable to join us for the full three-day camping experience, we encourage you to join us for the one-day Pelham Day event, along with other important decision-makers and political leaders. We have a helicopter landing area close to the activities for your convenience. Please RSVP to Owen March, Miyo? B'ilo Cultural Productions Manager at OwenMarch@pelhamcrk.example or Wendel Fusk, PCFN Councilor at Wfusk@pelhamcrk.example. We are looking forward to hosting you!

Page 3 - Signatures Names can be put in but I will need to add signatures after.
Page 4. 2023 Sponsors this will need to be editable as we get new ones in.
Page 5. Participant supplies check list. All of this is good just need to make it look better
Page 6. Agenda Dates need to change May 23-26 2023 This page also needs to be editable .. the days Dates need to change also.
Page 7 . Same info can be there.
All pages can use different photos where you need them..
Different logos on the sponsor page so that needs to be editable.
Daily Agenda needs to be editable .. definitely a better table

Things that need to be editable are dates (May 23-26th 2023)

I am just gathering some more photos for the brochure and will add them as I go .

Target Market(s)

Corporate partners

Colors
0054AA
0677BA
7BADD7
CADEEF
E8F1F8
0094D4
00A9DD
6FCCEA
C7EBF8
E9F6FB
00AB8E
00BBA5
67D7C9
C6EFE9
E9F9F6
59FF00
82FF00
B8FF75
E3FFCB
F4FFEA
FFF300
FFF600
FEFA6F
FFFEC7
FFFEE8
FFC000
F8CF3A
FAE287
FDF2CF
FEFAEE
F0912C
F2A743
F7CA91
FBE8D2
FDF5EE
EE7325
F08F49
F5BC92
FAE3D3
FDF4ED
EB3D1F
EC4F4E
F09395
F8D3D4
FCEDEE

Requirements
Must have
• The information that was provided
Nice to have
• We would like this to be very inviting and professional
Should not have
• cartoons or anything that looks cheap

```html
<!DOCTYPE html>
<html lang="en">
<head>
<meta charset="utf-8">
<title>Vola Executive Camping Experience – Brochure</title>
<link rel="stylesheet" href="https://fonts.googleapis.com/css2?family=Cormorant+Garamond:wght@500;600&family=Montserrat:wght@400;500;600&display=swap">
<style>
  :root {
    --backdrop: #e4e4e4;
    --paper-warm: #ece7e2;
    --paper-cool: #f4f4f4;
    --ink: #3a3a3a;
    --ink-soft: #6a6a6a;
    --night: #141c33;
    --night-deep: #0b1122;
    --cover-text: #e6e8ee;
    --accent: #0094d4;
    --shadow: rgba(0,0,0,0.18);
  }
  * { box-sizing: border-box; margin: 0; padding: 0; }
  html, body { width: 1200px; height: 800px; overflow: hidden; }
  body {
    background: var(--backdrop);
    font-family: "Montserrat", sans-serif;
    color: var(--ink);
    position: relative;
  }
  .page {
    position: absolute;
    top: 167px;
    width: 360px;
    height: 466px;
    overflow: hidden;
    box-shadow: 0 6px 18px var(--shadow);
  }
  /* Page 2: invitation */
  .page-invitation { left: 40px; background: var(--paper-warm); }
  .invitation-photo {
    position: absolute; left: 0; top: 0; width: 100%; height: 160px;
    background: linear-gradient(180deg, #c9cdd0 0%, #7d8a80 30%, #4f6148 55%, #b9b0a4 80%, var(--paper-warm) 100%);
  }
  .invitation-text {
    position: absolute; left: 28px; right: 28px; top: 168px;
    font-size: 5.9px; line-height: 1.42; color: var(--ink);
  }
  .invitation-text p { margin-bottom: 4.5px; }
  .invitation-text .closing { font-weight: 600; margin-top: 6px; }

  /* Page 3: signatures */
  .page-signatures { left: 400px; background: var(--paper-cool); }
  .signatures-title {
    position: absolute; left: 34px; top: 34px;
    font-family: "Cormorant Garamond", serif; font-weight: 600;
    font-size: 13px; letter-spacing: 0.22em; color: var(--ink);
  }
  .signature-list { position: absolute; left: 34px; top: 64px; list-style: none; }
  .signature-entry { margin-bottom: 16px; }
  .signature-line { display: block; width: 90px; height: 18px; border-bottom: 1px solid var(--ink-soft); margin-bottom: 4px; }
  .signer-name { font-size: 8px; font-weight: 500; letter-spacing: 0.04em; text-transform: uppercase; }
  .signer-role { font-size: 6px; font-style: italic; color: var(--ink-soft); }
  .gear-photo {
    position: absolute; left: 0; bottom: 0; width: 100%; height: 150px;
    background: linear-gradient(180deg, var(--paper-cool) 0%, #d9d4cc 30%, #8e7a60 60%, #5c5447 100%);
  }
  .spread-fold {
    position: absolute; left: 398px; top: 167px; width: 4px; height: 466px;
    background: linear-gradient(90deg, rgba(0,0,0,0.12), rgba(0,0,0,0));
  }

  /* Page 1: cover */
  .page-cover { left: 800px; background: var(--night); }
  .cover-photo {
    position: absolute; inset: 0;
    background:
      radial-gradient(ellipse at 40% 78%, rgba(214,150,60,0.55) 0%, rgba(214,150,60,0) 40%),
      linear-gradient(160deg, var(--night-deep) 0%, #1f2b4d 35%, #3a3550 55%, #2b2a22 75%, #1a1c14 100%);
  }
  .cover-brand {
    position: absolute; right: 34px; top: 60px; text-align: right;
    font-family: "Cormorant Garamond", serif; font-weight: 500;
    color: var(--cover-text); font-size: 34px; letter-spacing: 0.04em;
  }
  .cover-title {
    position: absolute; left: 34px; right: 34px; top: 170px; text-align: center;
    font-family: "Cormorant Garamond", serif; font-weight: 500;
    color: var(--cover-text);
  }
  .cover-title .event { font-size: 15px; letter-spacing: 0.22em; }
  .cover-title .edition { font-size: 11px; letter-spacing: 0.32em; margin-top: 6px; }
  .cover-host {
    position: absolute; left: 30px; bottom: 30px;
    display: flex; align-items: center; gap: 8px;
    font-family: "Montserrat", sans-serif; font-weight: 500;
    font-size: 9px; letter-spacing: 0.06em; text-transform: uppercase;
    color: var(--cover-text);
  }
  .cover-host .mark { width: 14px; height: 14px; border-radius: 50%; background: var(--accent); }
</style>
</head>
<body>

<section class="page page-invitation">
  <div class="invitation-photo" role="img" aria-label="Photo of a hiker walking across a sandy valley between green mountain ridges"></div>
  <div class="invitation-text">
    <p>Join us for an immersive cultural experience at Pelham Creek First Nation (PCFN) community, located in Northeastern BC. We invite you to participate in the Vola Camping Experience, a unique opportunity to forge relationships with our community, connect with our Chief and Council, and engage with industry leaders. Your participation in this grassroots event will earn your company credibility for the work it performs in PCFN territory.</p>
    <p>Through this experience, you'll gain an appreciation and understanding of our community and cultural values, while meeting with key office staff, industry C-Suite level executives, industry Indigenous relations staff, and local, regional, and provincial representatives in a positive and welcoming space. The recent Tarrow V. Ontario 2021 decision has significantly shifted how consultation and engagement will be managed on our lands. To help you better understand why managing cumulative effects is essential to PCFN, we welcome you to join us for a three-day camping experience from May 23 to May 26, 2023.</p>
    <p>The Vola Camping Experience offers a variety of activities, including a dinner visit to NAH 'B'ilo, the 12,500-year-old cave, where an archeological dig is currently underway, accompanied by our economic development corporation team from Raska Development LP. The event also includes traditional bush camping in elegant teepees/wall tents, dry meat making, and participation in our Pelham Day, a 30+ year cultural education and anti-racism event held on May 25, 2023. During Pelham Day, over 400+ students from School District #47 participate in traditional activities, including moose hide preparation, beaver skinning, archaeology dig, dry-meat making, trapping demonstrations, Bannock on a stick, storytelling, drumming, and tea dance around the campfire to the beat of our drums.</p>
    <p>Root yourself to the land, connect with your inner self, and be transformed alongside other important dignitaries as you partake in these multi-sensory experiences on our cultural grounds. This is our second combined camping/Pelham Day experience, and we hope to continue and build on it for future cultural tourism activities such as guided bush camps, hikes, and hunts.</p>
    <p>If you are unable to join us for the full three-day camping experience, we encourage you to join us for the one-day Pelham Day event, along with other important decision-makers and political leaders. We have a helicopter landing area close to the activities for your convenience. Please RSVP to Owen March, Miyo? B'ilo Cultural Productions Manager at OwenMarch@pelhamcrk.example or Wendel Fusk, PCFN Councilor at Wfusk@pelhamcrk.example.</p>
    <p class="closing">We are looking forward to hosting you!</p>
  </div>
</section>

<section class="page page-signatures">
  <h2 class="signatures-title">SIGNATURES</h2>
  <ul class="signature-list">
    <li class="signature-entry"><span class="signature-line"></span><div class="signer-name">Dorian Halvek</div><div class="signer-role">Chief PCFN</div></li>
    <li class="signature-entry"><span class="signature-line"></span><div class="signer-name">Name Goes Here</div><div class="signer-role">Position Goes Here</div></li>
    <li class="signature-entry"><span class="signature-line"></span><div class="signer-name">Name Goes Here</div><div class="signer-role">Position Goes Here</div></li>
    <li class="signature-entry"><span class="signature-line"></span><div class="signer-name">Name Goes Here</div><div class="signer-role">Position Goes Here</div></li>
  </ul>
  <div class="gear-photo" role="img" aria-label="Flat-lay photo of camping gear: camera, knives, hat, compass, canvas bag and folding shovel"></div>
</section>
<div class="spread-fold"></div>

<section class="page page-cover">
  <div class="cover-photo" role="img" aria-label="Night photo of campers around a glowing fire beside tents, under the Milky Way above a valley of town lights"></div>
  <div class="cover-brand">Vola Experience</div>
  <div class="cover-title">
    <div class="event">VOLA EXECUTIVE CAMPING EXPERIENCE</div>
    <div class="edition">PELHAM DAY 2023</div>
  </div>
  <div class="cover-host"><span class="mark"></span>Pelham Creek First Nation</div>
</section>

</body>
</html>
```